Wordpress template re-design of current website

We need a WordPress template design and new look for our existing website. Our existing site it located at www.velmoro.com.au We are a tech company and want a fresh, clean modern website that matches our brand, services and logo colors. Our main Services are hospitality solutions, Velmoro TV solution and managed networks, more information on these can come from our existing website.

Target Market(s)

We are a tech company so must have a modern feel for new technology

Industry/Entity Type

It Company

Number of Pages Required

5+ page

Font styles to use
Sans Serif

Requirements
Must have
• Be based on a wordpress templete design and match the services that we have in our existing website, in the testimonials want a place for video testimonials as well as text. Nice clean icons used for graphics to represent services.
Nice to have
• nice visual representation of our services in the way of clean icons etc
Should not have
• Clutter

```html
<!DOCTYPE html>
<html lang="en">
<head>
<meta charset="utf-8">
<title>Velmoro Wireless</title>
<link href="https://fonts.googleapis.com/css2?family=Lato:ital,wght@0,300;0,400;0,700;1,300;1,700;1,900&display=swap" rel="stylesheet">
<style>
  :root{
    --blue:#0d4a8c;
    --blue-dark:#0a3f7a;
    --ink:#222;
    --muted:#555;
    --topbar:#f7f7f7;
    --rule:#c9c9c9;
    --band:#f4f4f4;
  }
  *{box-sizing:border-box;margin:0;padding:0}
  html,body{width:1200px;height:1200px;overflow:hidden;background:#fff;font-family:"Lato",sans-serif;color:var(--ink)}
  .page{position:relative;width:1200px;height:1200px;overflow:hidden}

  .topbar{height:31px;background:var(--topbar);display:flex;align-items:center;justify-content:space-between;padding:0 160px;font-size:13px;color:#444}
  .topbar .call{display:flex;align-items:center;gap:5px}
  .topbar .links{display:flex;align-items:center;gap:20px;font-size:10px;color:#444}

  .header{height:84px;display:flex;align-items:center;justify-content:space-between;padding:0 160px;box-shadow:0 2px 4px rgba(0,0,0,.12);position:relative;z-index:2}
  .brand{display:flex;align-items:center;gap:8px;font-size:28px;color:var(--blue);font-weight:400}
  .brand .mark{width:14px;height:14px;border-radius:50%;background:var(--blue)}
  .nav{display:flex;align-items:center;gap:9px;font-size:11.5px;text-transform:uppercase;color:#222}
  .nav .active{color:var(--blue);font-weight:700}
  .nav .cta{margin-left:9px;background:var(--blue);color:#fff;font-weight:700;font-size:12.5px;padding:9px 16px;border-radius:3px}

  .hero{position:absolute;top:115px;left:0;width:1200px;height:400px;
    background:linear-gradient(90deg,#6b3c1e 0%,#a86a35 22%,#4a2a16 45%,#7a4a28 60%,#2c2420 75%,#8a5630 100%)}
  .hero .caption{position:absolute;left:160px;top:306px;width:460px;height:81px;border-left:2px solid #fff;
    background:linear-gradient(90deg,rgba(20,14,10,.92) 0%,rgba(20,14,10,.8) 60%,rgba(20,14,10,0) 100%);
    padding:18px 0 0 13px;color:#fff;font-style:italic;font-weight:700;font-size:19.5px;line-height:23.5px}

  .clients{position:absolute;top:515px;left:0;width:1200px;height:72px;background:rgba(240,240,240,.95);
    display:flex;align-items:center;justify-content:space-between;padding:0 165px}
  .clients span{font-size:14px;font-weight:700;color:#333;letter-spacing:.5px}

  .intro{position:absolute;top:587px;left:0;width:1200px;height:401px;text-align:center}
  .intro h1{margin-top:78px;font-size:34px;font-weight:700;color:var(--blue);letter-spacing:-.5px}
  .intro .tag{font-size:12.5px;text-transform:uppercase;color:#333;margin-top:2px}
  .rule{display:block;height:4px;background:var(--rule);margin:0 auto}
  .intro .rule{width:122px;margin-top:12px}
  .intro p{width:660px;margin:24px auto 0;font-size:12.5px;line-height:20px;color:#222}
  .intro p.lead{margin-top:20px;font-weight:700;font-size:12.5px}
  .btn{display:inline-block;margin-top:20px;background:var(--blue);color:#fff;font-weight:700;font-size:12.5px;padding:11px 20px 11px}

  .apps{position:absolute;top:988px;left:0;width:1200px;height:212px;background:var(--band);border-top:1px solid #ddd;text-align:center}
  .apps h2{margin-top:57px;font-size:41px;font-weight:300;color:#444}
  .apps .sub{font-size:16.5px;font-style:italic;font-weight:300;color:#444;margin-top:2px}
  .apps .rule{width:361px;margin-top:13px}
  .icons{position:absolute;top:197px;left:283px;width:620px;display:flex;justify-content:space-between}
</style>
</head>
<body>
<div class="page">
  <div class="topbar">
    <div class="call">
      <svg width="12" height="12" viewBox="0 0 12 12"><rect width="12" height="12" rx="2" fill="#555"/><path d="M3.5 2.8c.4-.3.9 0 1.1.5l.4.9c.1.3 0 .6-.2.8l-.4.3c.4.9 1 1.5 1.9 1.9l.3-.4c.2-.2.5-.3.8-.2l.9.4c.5.2.8.7.5 1.1l-.4.6c-.3.4-.9.6-1.4.4C5 8.5 3.5 7 2.9 4.6c-.2-.5 0-1.1.4-1.4z" fill="#fff"/></svg>
      CALL US: 1300 555 014
    </div>
    <div class="links">
      <svg width="14" height="14" viewBox="0 0 14 14"><circle cx="6" cy="6" r="4.8" fill="none" stroke="#777" stroke-width="1.2"/><path d="M9.5 9.5l3.5 3.5" stroke="#777" stroke-width="1.2"/></svg>
      <span>Blog</span><span>Career</span><span>Contact Us</span>
    </div>
  </div>

  <header class="header">
    <div class="brand"><span>Velmoro</span><span class="mark"></span></div>
    <nav class="nav">
      <span class="active">Home</span><span>Services</span><span>About</span><span>Our Work</span><span>Contact</span><span>Portal</span>
      <span class="cta">GET STARTED</span>
    </nav>
  </header>

  <section class="hero" role="img" aria-label="Warm hotel lounge with timber-panelled walls, leather armchairs and a window over the city at night">
    <div class="caption">Get On The Fastest,<br>Most Flexible Internet Access System</div>
  </section>

  <div class="clients">
    <span>HARBOR</span><span>LINDELL</span><span>AURELLE</span><span>TRAILWAY</span><span>KESTREL</span><span>ROAMLY</span><span>CORVANE</span><span>SEABROOK</span>
  </div>

  <section class="intro">
    <h1>Velmoro Wireless</h1>
    <div class="tag">Creating solutions that work.</div>
    <span class="rule"></span>
    <p><strong>Velmoro Wireless</strong> is at the forefront of revolutionising high-speed internet access (HSIA) services. We offer complete wireless solutions: Right from developing individual components such as hotspots and access controllers, to installation of the internet infrastructure. Once we setup the HSIA for our clients, we back it up with round-the-clock tech support.</p>
    <p class="lead">Velmoro’s expertise in wireless technology has attracted a growing client base from all over Australia.</p>
    <a class="btn">Learn more about Us</a>
  </section>

  <section class="apps">
    <h2>We Create Intuitive Applications</h2>
    <div class="sub">The sole focus of Velmoro’s hospitality solutions is to make them an intuitive, guest friendly experience.</div>
    <span class="rule"></span>
    <div class="icons">
      <svg width="52" height="20" viewBox="0 0 52 20"><rect x="1" y="2" width="50" height="18" rx="2" fill="var(--blue)"/><path d="M22 8h8M26 4v8" stroke="#fff" stroke-width="2"/></svg>
      <svg width="52" height="20" viewBox="0 0 52 20"><path d="M18 2l8 8 8-8" stroke="#555" stroke-width="2" fill="none"/><rect x="1" y="10" width="50" height="12" rx="2" fill="none" stroke="#555" stroke-width="2"/></svg>
      <svg width="44" height="20" viewBox="0 0 44 20"><circle cx="22" cy="22" r="19" fill="none" stroke="#555" stroke-width="2.5"/><circle cx="22" cy="22" r="12" fill="none" stroke="#555" stroke-width="2.5"/></svg>
      <svg width="24" height="20" viewBox="0 0 24 20"><rect x="3" y="6" width="18" height="16" fill="none" stroke="#555" stroke-width="2"/></svg>
      <svg width="50" height="20" viewBox="0 0 50 20"><path d="M8 20a16 16 0 0 1 10-12M42 20a16 16 0 0 0-10-12" stroke="#555" stroke-width="4" fill="none"/></svg>
    </div>
  </section>
</div>
</body>
</html>
```